business card with 2 locations on 1 card

I need a modern looking business card that I would use at 2 different locations. Possibly 1 location on 1 side and other location on other side. One should be able to distinguish the 2 locations immediately before having to read the address or description on card. You can take a look at my website to see what I'm drawn to. The logo is brand new that I just purchased on Craft Hive. I want to emphasize family.
Updates

Let's not use the yellow and blue colors. Added Thursday, August 31, 2017

Target Market(s)

women and children

Industry/Entity Type

Health And Wellness

Contact Information for Business Card

Business name: Willow Brook Chiropractic & Acupuncture
My name: Lorin Daske
Job title: DC, MAOM, LAc (CA), CNS

Location 1
Address: 4817 Marlowe Blvd, Suite B-100, Frisco, TX 75034
Phone: (469) 555-0182
Fax: (972) 555-0137

Location 2
Address: 1936 Belvane Road, Suite 100, Plano, TX 75075
Phone: (469) 555-0169
Fax: (972) 555-0137

Email: drlorindaske@mailnest.example
Website: www.drlorindaske.example

Font styles to use
Serif
Sans Serif

Colors

Designer to choose colors to be used in the design.

Requirements
Must have
• distinction between 2 locations.
Nice to have
• Colors preference below is there. But I like to see what you come up with too!

```html
<!DOCTYPE html>
<html lang="en">
<head>
<meta charset="utf-8">
<title>Willow Brook business cards</title>
<link href="https://fonts.googleapis.com/css2?family=Mulish:wght@400;600;800&display=swap" rel="stylesheet">
<style>
  :root {
    --teal: #236b6c;
    --green: #a9d37a;
    --white: #ffffff;
    --ink: #3a4a4a;
    --page: #ececec;
  }
  html, body {
    margin: 0;
    width: 1200px;
    height: 874px;
    overflow: hidden;
    background: var(--page);
    font-family: "Mulish", sans-serif;
  }
  .sheet {
    position: relative;
    width: 1200px;
    height: 874px;
  }
  .card {
    position: absolute;
    left: 260px;
    width: 680px;
    height: 389px;
    overflow: hidden;
    box-shadow: 0 6px 18px rgba(0,0,0,.15);
  }
  .card--frisco { top: 30px; background: var(--white); --band: var(--teal); --fg: var(--teal); --text: var(--ink); }
  .card--plano  { top: 455px; background: var(--teal); --band: var(--white); --fg: var(--white); --text: var(--white); }

  .band { position: absolute; height: 14px; }
  .band--top-main   { top: 0; left: 58%; width: 24%; background: var(--band); }
  .band--top-accent { top: 0; left: 82%; width: 18%; background: var(--green); }
  .band--bottom-accent { bottom: 0; left: 0; width: 32%; background: var(--green); }
  .band--bottom-main   { bottom: 0; left: 32%; width: 68%; background: var(--band); }

  .brand {
    position: absolute;
    left: 48px;
    top: 52px;
    display: flex;
    align-items: center;
    gap: 16px;
  }
  .brand__mark {
    width: 70px;
    height: 70px;
    border-radius: 50%;
    border: 3px solid var(--fg);
    box-sizing: border-box;
  }
  .brand__name {
    color: var(--fg);
    font-weight: 600;
    font-size: 17px;
    line-height: 1.25;
    letter-spacing: .5px;
  }

  .person {
    position: absolute;
    left: 420px;
    top: 62px;
    color: var(--text);
  }
  .person__name {
    margin: 0;
    font-weight: 800;
    font-size: 24px;
    color: var(--fg);
  }
  .person__title {
    margin: 2px 0 22px;
    font-size: 12.5px;
  }
  .person__contact {
    margin: 0;
    font-size: 12.5px;
    line-height: 1.6;
  }

  .office {
    position: absolute;
    left: 48px;
    top: 196px;
    color: var(--text);
    font-size: 16px;
    line-height: 1.35;
  }
  .office__label {
    margin: 0;
    font-weight: 800;
    font-size: 17px;
    color: var(--green);
  }
  .card--frisco .office__label { color: var(--teal); }
  .office__line { margin: 0; }
</style>
</head>
<body>
<main class="sheet">

  <section class="card card--frisco" aria-label="Frisco office card">
    <div class="band band--top-main"></div>
    <div class="band band--top-accent"></div>
    <div class="band band--bottom-accent"></div>
    <div class="band band--bottom-main"></div>

    <div class="brand">
      <div class="brand__mark"></div>
      <div class="brand__name">Willow Brook<br>Chiropractic &amp; Acupuncture</div>
    </div>

    <div class="person">
      <h2 class="person__name">Lorin Daske</h2>
      <p class="person__title">DC, MAOM, LAc (CA), CNS</p>
      <p class="person__contact">E: drlorindaske@mailnest.example<br>W: www.drlorindaske.example</p>
    </div>

    <div class="office">
      <p class="office__label">Frisco’s Office</p>
      <p class="office__line">Address: 4817 Marlowe Blvd, Suite B-100, Frisco, TX 75034</p>
      <p class="office__line">Phone: (469) 555-0182</p>
      <p class="office__line">Fax: (972) 555-0137</p>
    </div>
  </section>

  <section class="card card--plano" aria-label="Plano office card">
    <div class="band band--top-main"></div>
    <div class="band band--top-accent"></div>
    <div class="band band--bottom-accent"></div>
    <div class="band band--bottom-main"></div>

    <div class="brand">
      <div class="brand__mark"></div>
      <div class="brand__name">Willow Brook<br>Chiropractic &amp; Acupuncture</div>
    </div>

    <div class="person">
      <h2 class="person__name">Lorin Daske</h2>
      <p class="person__title">DC, MAOM, LAc (CA), CNS</p>
      <p class="person__contact">E: drlorindaske@mailnest.example<br>W: www.drlorindaske.example</p>
    </div>

    <div class="office">
      <p class="office__label">Plano’s Office</p>
      <p class="office__line">Address: 1936 Belvane Road, Suite 100, Plano, TX 75075</p>
      <p class="office__line">Phone: (469) 555-0169</p>
      <p class="office__line">Fax: (972) 555-0137</p>
    </div>
  </section>

</main>
</body>
</html>
```